'Cradle Ahead' promotional brochure

We have designed a 6 week program to educate impending first-time parents about the things they need to know to survive the first 6 months. Sessions delivered by general practitioner/family doctor, dietician, physiotherapist, speech pathologist and psychologist. Our promotional blurb is: 'A comprehensive education program for first-time parents-to-be, delivered over 6 weeks by health professionals in your community, about everything you need to know to look after your baby (and yourself!) in the first 6 months'. I now want to put together a promotional brochure to be distributed to those couples who express an interest which will provide further details of what will be delivered in the course.
Updates
In terms of layout, I envisaged a double sided A4 size, foldable into 3 sections, but very happy to be guided on this.
Target Market(s)
To appeal to a young, well educated demographic. First time parents couples.
Industry/Entity Type
Medical
Font styles to use
Other font styles liked:
- Playfair Display
Requirements
Must have
- Playfair display font to be consistent with our logo (attached). Logo also included please. Some consistency with colours of logo please.
Nice to have
- I am a doctor, and have no creative genes! But prefer a clean and professional appearance overall. Not too cluttered in overall appearance.
Should not have
- No cheesy pictures of babies.

```html
<!DOCTYPE html>
<html lang="en">
<head>
<meta charset="utf-8">
<title>Cradle Ahead brochure</title>
<link rel="stylesheet" href="https://fonts.googleapis.com/css2?family=Playfair+Display:wght@400;700;900&family=Lato:wght@400;700&display=swap">
<style>
:root{
  --green:#6cb94b;
  --green-dark:#5aa53c;
  --grey:#8e8f90;
  --bg:#d5d6d8;
  --text:#5b5b5b;
  --title:#4f4f4f;
  --paper:#ffffff;
}
*{box-sizing:border-box;margin:0;padding:0}
html,body{width:879px;height:1200px;overflow:hidden;background:var(--bg)}
body{position:relative;font-family:'Lato',sans-serif;color:var(--text)}
.sheet{position:absolute;left:102px;width:690px;height:488px;display:flex;box-shadow:0 1px 3px rgba(0,0,0,.12)}
.sheet--outside{top:97px}
.sheet--inside{top:616px}
.panel{position:relative;width:230px;height:100%;overflow:hidden;background:var(--paper)}
.panel--green{background:var(--green);color:#fff}
.pill{display:inline-block;font-family:'Playfair Display',serif;font-weight:700;font-size:15px;line-height:1;padding:2px 9px 3px;border-radius:10px;background:var(--green);color:#fff;letter-spacing:.5px}
.panel--green .pill{background:#fff;color:var(--green)}
.session{font-size:8px;font-weight:700;margin-top:8px;text-transform:uppercase}
.copy{font-size:8px;line-height:1.35;text-align:justify}
.week{margin-bottom:14px}
.topics{list-style:none;font-size:8px;line-height:1.8;margin-top:3px}
.topics li::before{content:"•";margin-right:6px}
.photo{position:absolute}
.brand{display:flex;align-items:center;gap:8px;font-family:'Playfair Display',serif;font-size:13px;line-height:1.05;color:var(--green);text-transform:uppercase}
.brand__mark{width:14px;height:14px;background:var(--green);flex:none}
.panel--green .brand{color:#fff}
.panel--green .brand__mark{background:#fff}
.contact{position:absolute;left:0;right:0;text-align:center;font-size:8.5px;line-height:1.3}
.icon{display:block;margin:0 auto 4px}
.web-pill{position:absolute;left:27px;width:184px;top:440px;background:#fff;color:var(--green);border-radius:10px;font-size:8.5px;font-weight:700;text-align:center;padding:4px 0}
.title{font-family:'Playfair Display',serif;font-weight:900;text-align:center;line-height:.95;text-transform:uppercase}
</style>
</head>
<body>

<!-- Outside sheet -->
<section class="sheet sheet--outside">
  <article class="panel">
    <div class="photo" role="img" aria-label="Soft faded photo of an expecting couple holding a pregnant belly" style="left:0;right:0;bottom:0;height:230px;background:linear-gradient(180deg,#fff 0%,#f1ece9 35%,#e3d7d3 100%)"></div>
    <div style="position:absolute;left:18px;right:20px;top:40px">
      <div class="week">
        <span class="pill">WEEK 5</span>
        <p class="session">Session 1</p>
        <p class="copy">Clinical Psychologist Dr Maren Holt will share information about bonding &amp; attachment with your baby, how to promote their social &amp; emotional development and how to manage separation anxiety. She will also discuss positive parenting approaches.</p>
      </div>
      <div class="week">
        <span class="pill">WEEK 6</span>
        <p class="session">Session 1</p>
        <p class="copy">Secret Men's Business – a men-only session (including beer!) with a new father for frank discussion about the road ahead. Mums will do a shopping excursion with the GP &amp; Dietician to the local grocer to look at baby products and food – the good and the bad!</p>
        <p class="session">Session 2</p>
        <p class="copy">Program review, reflection and evaluation and future session planning when baby is 6 months of age.</p>
      </div>
    </div>
  </article>

  <article class="panel panel--green">
    <div class="photo" role="img" aria-label="Green-tinted photo of a smiling pregnant woman" style="left:30px;right:0;top:20px;bottom:0;background:radial-gradient(ellipse at 55% 40%,rgba(255,255,255,.22),rgba(255,255,255,0) 65%)"></div>
    <div class="brand" style="position:absolute;left:42px;top:190px"><span class="brand__mark"></span><span>Wattlebrook<br>Health &amp;<br>Medical</span></div>
    <div class="contact" style="top:250px">
      <svg class="icon" width="12" height="12" viewBox="0 0 12 12"><circle cx="6" cy="6" r="6" fill="#fff"/><path d="M6 2.5a2 2 0 0 0-2 2c0 1.6 2 4 2 4s2-2.4 2-4a2 2 0 0 0-2-2z" fill="#6cb94b"/></svg>
      Wattlebrook Village, Shop 11<br>210 Wattle Way<br>Wattlebrook NSW 2999
    </div>
    <div class="contact" style="top:308px">
      <svg class="icon" width="12" height="12" viewBox="0 0 12 12"><circle cx="6" cy="6" r="6" fill="#fff"/><path d="M4 3h1.2l.6 1.6-.8.6a4 4 0 0 0 1.8 1.8l.6-.8 1.6.6V8a1 1 0 0 1-1 1A5 5 0 0 1 3 4a1 1 0 0 1 1-1z" fill="#6cb94b"/></svg>
      02 5550 0188
    </div>
    <div class="contact" style="top:348px">
      <svg class="icon" width="12" height="12" viewBox="0 0 12 12"><circle cx="6" cy="6" r="6" fill="#fff"/><rect x="3" y="4.5" width="6" height="4" fill="#6cb94b"/><rect x="4" y="3" width="4" height="2" fill="#6cb94b"/></svg>
      02 5550 0199
    </div>
    <div class="contact" style="top:390px">
      <svg class="icon" width="12" height="12" viewBox="0 0 12 12"><circle cx="6" cy="6" r="6" fill="#fff"/><rect x="3" y="4" width="6" height="4" fill="#6cb94b"/><path d="M3 4l3 2.2L9 4" stroke="#fff" stroke-width=".7" fill="none"/></svg>
      reception@wattlebrookhealth.com.au
    </div>
    <div class="web-pill">www.wattlebrookhealth.com.au</div>
  </article>

  <article class="panel">
    <div class="brand" style="position:absolute;left:40px;top:34px;color:var(--title)"><span class="brand__mark"></span><span>Wattlebrook<br>Health &amp;<br>Medical</span></div>
    <p style="position:absolute;left:0;right:0;top:92px;text-align:center;font-size:7.5px">www.wattlebrookhealth.com.au</p>
    <svg style="position:absolute;left:12px;top:122px" width="208" height="180" viewBox="0 0 208 180" role="img" aria-label="Photo of hands forming a heart over a pregnant belly">
      <defs><radialGradient id="skin" cx=".5" cy=".45" r=".6"><stop offset="0" stop-color="#e9c2a9"/><stop offset="1" stop-color="#c99780"/></radialGradient></defs>
      <path d="M104 178C50 130 0 98 0 50 0 20 22 0 52 0c24 0 40 12 52 30C116 12 132 0 156 0c30 0 52 20 52 50 0 48-50 80-104 128z" fill="url(#skin)"/>
    </svg>
    <h1 class="title" style="position:absolute;left:0;right:0;top:330px;font-size:34px;color:var(--title)">Cradle<br><span style="color:var(--green)">Ahead</span></h1>
    <div style="position:absolute;left:0;right:0;top:412px;text-align:center">
      <span class="pill">6 WEEKS</span>
      <p style="font-family:'Playfair Display',serif;font-size:15px;margin-top:4px;color:var(--title)">Educational Program</p>
      <p style="font-family:'Playfair Display',serif;font-size:12px;color:var(--title)">For First Time Parents</p>
    </div>
  </article>
</section>

<!-- Inside sheet -->
<section class="sheet sheet--inside">
  <article class="panel">
    <div style="position:absolute;left:0;right:0;top:0;height:223px;background:var(--grey);color:#fff">
      <h2 class="title" style="margin-top:34px;font-size:32px">Cradle<br>Ahead</h2>
      <p style="font-family:'Playfair Display',serif;font-size:9.4px;line-height:1.4;padding:0 17px 0 26px;margin-top:16px">A comprehensive <b>education program</b> for first-time parents-to-be, delivered <b>over 6 weeks by health professionals</b> in your community, about everything you need to know to look after your baby (and yourself!) in the first 6 months.</p>
    </div>
    <div class="photo" role="img" aria-label="Photo of a sleeping newborn holding a parent's finger" style="left:0;right:0;top:223px;height:153px;background:linear-gradient(135deg,#e9cfbf 0%,#f2e2d6 45%,#c9dba2 100%)"></div>
    <div class="brand" style="position:absolute;left:42px;top:410px;color:var(--title)"><span class="brand__mark"></span><span>Wattlebrook<br>Health &amp;<br>Medical</span></div>
  </article>

  <article class="panel panel--green">
    <div class="photo" role="img" aria-label="Photo of a happy couple looking at a pregnancy test" style="left:0;right:0;top:0;height:60px;background:linear-gradient(90deg,#cfc3b8,#e6d2c2 50%,#a98f7c)"></div>
    <div style="position:absolute;left:22px;right:18px;top:80px">
      <div class="week">
        <span class="pill">WEEK 1</span>
        <p class="copy" style="margin-top:8px;text-align:left">GP Dr Alice Brandt will share information for Mum's own health after delivery.</p>
        <p style="font-size:8px;font-weight:700;margin-top:4px">Topics include:</p>
        <ul class="topics" style="margin-left:12px">
          <li>Vaccinations in pregnancy</li>
          <li>Bleeding, bladder and bowel after delivery</li>
          <li>Breastfeeding, engorgement and mastitis</li>
          <li>Bottle feeding</li>
          <li>Post-natal anxiety &amp; depression</li>
          <li>Intimacy and contraception</li>
        </ul>
      </div>
      <div class="week" style="margin-top:18px">
        <span class="pill">WEEK 2</span>
        <p class="session">Session 1</p>
        <p class="copy">Clinical Psychologist Dr Maren Holt will discuss changes in relationships as couples becomes parents, gender roles in parenting and post-natal depression.</p>
        <p class="session">Session 2</p>
        <p class="copy">Physiotherapist Tessa Lowry will present advice for Mums regarding exercise during and after pregnancy, looking after the pelvic floor during and after pregnancy, and abdominal muscle separation management. She will also provide advice for promoting babies' neck strength and minimising the risk of flat spots on the head and encouraging gross motor skills in the first 6 months</p>
      </div>
    </div>
  </article>

  <article class="panel">
    <div style="position:absolute;left:22px;right:16px;top:26px">
      <div class="week">
        <span class="pill">WEEK 3</span>
        <p class="session">Session 1</p>
        <p class="copy">Dietician Nina Carvell provides advice for Mums regarding healthy eating during pregnancy and lactation, normal weight gain during pregnancy and realistic weight loss after. She will also discuss the evidence regarding breastfeeding VS bottle-feeding, normal infant weight gain and introducing solids (including those with potential for allergy).</p>
        <p class="session">Session 2</p>
        <p class="copy">Paediatric Speech Pathologist Ruth Ambler will share information about latching and breast-feeding troubles &amp; tongue tie, advice about dummies and finger-sucking, introducing solids &amp; feeding (including 'pouch' food), encouraging language development and current evidence about electronic devices impacting language development.</p>
      </div>
      <div class="week">
        <span class="pill">WEEK 4</span>
        <p class="copy" style="margin-top:8px">GP Dr Alice Brandt will share advice about your babies' health in the first 6 months, including:</p>
        <ul class="topics" style="margin-top:8px">
          <li>Skin of newborns</li>
          <li>Sleeping</li>
          <li>Crying</li>
          <li>Immunisations</li>
          <li>Fever and infections</li>
          <li>Diarrhoea and constipation</li>
          <li>Teething</li>
          <li>Understanding a baby's signals</li>
        </ul>
      </div>
    </div>
  </article>
</section>

</body>
</html>
```